Coffee roasting needs homepage with web shop

small roasting (no cafe!) needs a simple website with a web shop. We sell coffee to dealers and end customers. The shop should be for end consumers as well as for B2B customers. A login should be available. The design should be modern and at the same time classic with subtle (dark) colors. We need the tabs "Coffee, Shop, Contact, Coffee, Coffee, Login, About Us, Imprint, Privacy" Logo nr 1 should be used from attached file

Target Market(s)

B2B

Number of Pages Required

5+ page

Font styles to use
Sans Serif

Colors

Designer to choose only greyscale colors for use in the design.

Requirements
Must have
• Webshop

```html
<!DOCTYPE html>
<html lang="en">
<head>
<meta charset="utf-8">
<title>Kornhaus Roastery – Coffee &amp; Shop</title>
<link rel="stylesheet" href="https://fonts.googleapis.com/css2?family=Open+Sans:wght@400;600;700;800&family=Oswald:wght@400;500&display=swap">
<style>
:root{
  --orange:#df6b1d;
  --orange-soft:#efb592;
  --brown:#6a3b1f;
  --ink:#2a2a2a;
  --dark:#3d3b3c;
  --footer:#6f6d6e;
  --grey-btn:#9a9899;
  --search:#d9d5d5;
  --white:#ffffff;
}
*{box-sizing:border-box;margin:0;padding:0}
html,body{width:1200px;height:2486px;overflow:hidden;background:var(--white)}
body{font-family:"Open Sans",sans-serif;color:var(--ink);position:relative}
.abs{position:absolute}

/* utility bar */
.util-bar{left:0;top:0;width:1200px;height:37px;background:var(--orange)}
.util-bar ul{list-style:none;position:absolute;left:566px;top:10px;display:flex;font-size:12px;font-weight:600;letter-spacing:.6px;color:var(--white)}
.util-bar li{padding:0 16px;border-left:2px solid var(--white);line-height:16px}
.util-bar li:first-child{border-left:none;padding-left:0}

/* header */
.brand{left:197px;top:48px;width:126px;height:126px;border:2px solid #222;border-radius:50%;display:flex;align-items:center;justify-content:center}
.brand span{font-size:21px;font-weight:600;color:var(--ink)}
.search{left:416px;top:71px;width:407px;height:38px;background:var(--search);border-radius:3px}
.search svg{position:absolute;right:14px;top:8px}
.divider-v{left:849px;top:74px;width:1px;height:36px;background:#bbb}
.login-btn{left:876px;top:77px;width:108px;height:28px;background:var(--grey-btn);border-radius:2px;color:var(--white);font-size:10.5px;line-height:28px;text-align:center}
.main-nav{left:416px;top:147px;display:flex;list-style:none;font-size:15.5px;font-weight:700;color:var(--brown);letter-spacing:.2px}
.main-nav li{margin-right:38px}

/* hero */
.hero{left:0;top:188px;width:1200px;height:401px;
  background:
    linear-gradient(180deg,rgba(255,255,255,.25) 0%,rgba(0,0,0,0) 30%,rgba(0,0,0,.25) 100%),
    linear-gradient(100deg,#2e2e2e 0%,#5c5c5c 25%,#9c9c9c 45%,#cfcfcf 62%,#7a7a7a 80%,#3a3a3a 100%)}
.hero-title{left:200px;top:300px}
.hero-title .l1{font-weight:800;font-size:70px;color:var(--white);letter-spacing:-1px;line-height:80px}
.hero-title .l2,.hero-title .l3{font-family:"Oswald",sans-serif;font-size:46px;font-weight:400;color:var(--orange);letter-spacing:-2px;line-height:54px}
.hero-title .l2{padding-left:42px}
.hero-title .l3{padding-left:55px}
.hero-title .l3 em{font-style:normal;color:var(--white)}
.hero-notch{left:0;top:541px}

/* categories */
.cat-img{top:647px;width:249px;height:191px}
.cat-cap{top:846px;width:260px;text-align:center;font-size:15px;font-weight:700;color:var(--brown)}

.section-head{left:204px;top:896px;font-size:20px;font-weight:800;color:var(--brown);letter-spacing:.3px;display:flex;align-items:center}
.section-head svg{margin-left:16px}

/* product card */
.product{width:220px}
.product .photo{width:160px;height:190px;margin:0 auto}
.product .name{margin-top:24px;text-align:center;font-size:13.5px;font-weight:700;line-height:16px;color:var(--brown);white-space:nowrap}
.product .tags{margin-top:12px;height:24px;position:relative}
.tag{position:absolute;font-size:11.5px;font-weight:800;padding:2px 8px;color:var(--white)}
.tag.new{left:0;top:4px;background:var(--orange)}
.tag.sale{right:0;top:0;background:#6b6b6b}
.product .rule{margin-top:10px;height:4px;background:var(--orange)}
.product .rule+.rule{margin-top:0;height:5px;background:var(--orange-soft)}
.product .price{margin-top:12px;text-align:center;font-size:20px;font-weight:800;color:var(--ink)}
.product .price s{color:#8a8a8a;margin-right:10px}

/* product photo placeholders: soft cut-out tones on the page colour */
.ph-light-black{background:radial-gradient(ellipse 45% 50% at 50% 48%,#2a2a2a 0%,#3c3c3c 55%,rgba(255,255,255,0) 100%)}
.ph-light-silver{background:radial-gradient(ellipse 50% 48% at 50% 50%,#9a9a9a 0%,#6a6a6a 55%,rgba(255,255,255,0) 100%)}
.ph-light-red{background:radial-gradient(ellipse 40% 50% at 58% 45%,#c8282a 0%,#7a1a1c 40%,#222 60%,rgba(255,255,255,0) 100%)}
.ph-dark-silver{background:radial-gradient(ellipse 46% 50% at 50% 48%,#9c9c9c 0%,#1e1e1e 60%,rgba(61,59,60,0) 100%)}
.ph-dark-black{background:radial-gradient(ellipse 45% 50% at 50% 48%,#5a3a26 0%,#1c1c1c 55%,rgba(61,59,60,0) 100%)}
.ph-dark-steel{background:radial-gradient(ellipse 44% 50% at 50% 48%,#d0d0d0 0%,#8c8c8c 55%,rgba(61,59,60,0) 100%)}

/* dark band */
.dark-band{left:0;top:1377px;width:1200px;height:750px;background:var(--dark)}
.promo{left:202px;top:1419px;width:803px;height:137px;background:linear-gradient(90deg,#ece3d8 0%,#c89a70 25%,#8a5430 50%,#4a2a1a 75%,#3b2418 100%)}
.promo-text{left:740px;top:1440px;width:230px;text-align:center;color:var(--white);font-size:26px;font-weight:800;line-height:31px}
.promo-btn{display:inline-block;margin-top:6px;background:var(--orange);font-size:15px;padding:1px 16px;line-height:24px;border-radius:2px}
.tabs{left:212px;top:1582px;display:flex;align-items:center;font-size:21px;font-weight:800;color:var(--white)}
.tabs .sep{width:6px;height:40px;background:#c9c9c9;margin:0 26px 0 28px}
.tabs .active{color:var(--orange)}
.dark-band-products .product .name{color:var(--white)}
.dark-band-products .product .rule+.rule{background:#8a5334}
.dark-band-products .product .price{color:var(--white)}
.dark-band-products .product .price s{color:var(--white)}
.dark-band-products .product .price b{color:var(--orange)}
.dark-band-products .tag.sale{background:#8a8a8a}

.beans{left:936px;top:2066px;width:258px;height:142px;border-radius:46% 54% 50% 50%/55% 48% 52% 45%;background:radial-gradient(ellipse at 55% 40%,#8a5a44 0%,#5e3323 55%,#3e1f14 100%)}

/* contact strip */
.contact-strip{left:189px;top:2150px;display:flex;align-items:center;font-size:15px;color:var(--ink)}
.contact-strip .dot{width:32px;height:32px;border-radius:50%;background:var(--orange);margin-left:22px}
.contact-strip .dot:first-of-type{margin-left:12px}

/* footer */
.site-footer{left:0;top:2213px;width:1200px;height:273px;background:var(--footer)}
.footer-brand{left:185px;top:2293px;width:124px;height:124px;border:2px solid #1e1e1e;border-radius:50%;display:flex;align-items:center;justify-content:center;font-size:20px;font-weight:600;color:#1e1e1e}
.f-col{top:2278px;font-size:11px;color:#111}
.f-col h4{font-size:15.5px;font-weight:700;color:var(--orange);margin-bottom:16px}
.f-col p{line-height:30px}
.f-rule{top:2278px;width:1px;height:146px;background:#9a9899}
.news-input{width:146px;height:25px;background:var(--white);border-radius:2px;font-size:9px;color:#aaa;padding:5px 7px;margin-top:10px}
.news-btn{display:inline-block;margin:14px 0 0 36px;background:#111;color:var(--white);font-size:8.5px;font-weight:700;padding:3px 10px;border-radius:2px}
</style>
</head>
<body>

<nav class="util-bar abs">
  <ul><li>My Account</li><li>Checkout</li><li>Log In</li><li>English</li><li>USD</li></ul>
</nav>

<div class="brand abs"><span>Kornhaus</span></div>

<div class="search abs">
  <svg width="22" height="22" viewBox="0 0 22 22" fill="none" stroke="#444" stroke-width="1.8"><circle cx="9" cy="9" r="7"/><line x1="14" y1="14" x2="20" y2="20"/></svg>
</div>
<div class="divider-v abs"></div>
<div class="login-btn abs">Log in / Register</div>

<ul class="main-nav abs">
  <li>COFFEE</li><li>SHOP</li><li>CONTACT</li><li>ABOUT US</li><li>IMPRINT</li><li>PRIVACY</li>
</ul>

<section class="hero abs" role="img" aria-label="Black and white photograph of a coffee roastery interior"></section>
<div class="hero-title abs">
  <div class="l1">MAKE</div>
  <div class="l2">A STANDARD</div>
  <div class="l3">SOMETHING <em>SPECIAL</em></div>
</div>
<svg class="hero-notch abs" width="1200" height="48" viewBox="0 0 1200 48">
  <circle cx="426" cy="1" r="6" fill="none" stroke="#fff" stroke-width="2"/>
  <circle cx="454" cy="1" r="6.5" fill="#fff"/>
  <circle cx="482" cy="1" r="6" fill="none" stroke="#fff" stroke-width="2"/>
  <circle cx="510" cy="1" r="6" fill="none" stroke="#fff" stroke-width="2"/>
  <polygon points="490,48 612,6 734,48" fill="#fff"/>
</svg>

<div class="cat-img abs" style="left:204px;background:radial-gradient(circle at 50% 50%,#5a5a5a 0%,#b5b5b5 60%,#d4d4d4 100%)" role="img" aria-label="Top view of many coffee cups"></div>
<div class="cat-img abs" style="left:478px;background:radial-gradient(ellipse at 50% 40%,#f2f2f2 0%,#cfcfcf 45%,#5e5e5e 100%)" role="img" aria-label="Cappuccino with latte art on a saucer"></div>
<div class="cat-img abs" style="left:752px;background:linear-gradient(160deg,#3a3a3a 0%,#6e6e6e 45%,#8e8e8e 70%,#2e2e2e 100%)" role="img" aria-label="Black coffee cup on a wooden table with leaves"></div>
<div class="cat-cap abs" style="left:198px">SPECIAL CHOICES</div>
<div class="cat-cap abs" style="left:480px">GREAT CAPPUCCINOS</div>
<div class="cat-cap abs" style="left:745px">FRESHLY ROASTED BEAN COFFEES</div>

<h2 class="section-head abs">FEATURED PRODUCTS
  <svg width="30" height="14" viewBox="0 0 30 14"><polygon points="0,0 30,0 15,14" fill="#bdbdbd"/></svg>
</h2>

<article class="product abs" style="left:209px;top:960px">
  <div class="photo ph-light-black" role="img" aria-label="Black automatic espresso machine with latte glass"></div>
  <p class="name">Lorem ipsum dolor sit<br>amet, consectetur<br>adipiscing elit, sed do</p>
  <div class="tags"><span class="tag new">NEW</span><span class="tag sale">SALE</span></div>
  <div class="rule"></div><div class="rule"></div>
  <p class="price"><s>$120</s>$90</p>
</article>
<article class="product abs" style="left:502px;top:963px">
  <div class="photo ph-light-silver" role="img" aria-label="Silver bean-to-cup coffee machine with two drinks"></div>
  <p class="name">Lorem ipsum dolor sit<br>amet, consectetur<br>adipiscing elit, sed do</p>
  <div class="tags"><span class="tag new">NEW</span><span class="tag sale">SALE</span></div>
  <div class="rule"></div><div class="rule"></div>
  <p class="price"><s>$120</s>$90</p>
</article>
<article class="product abs" style="left:782px;top:961px">
  <div class="photo ph-light-red" role="img" aria-label="Red and black capsule coffee machine"></div>
  <p class="name">Lorem ipsum dolor sit<br>amet, consectetur<br>adipiscing elit, sed do</p>
  <div class="tags"><span class="tag new">NEW</span><span class="tag sale">SALE</span></div>
  <div class="rule"></div><div class="rule"></div>
  <p class="price"><s>$120</s>$90</p>
</article>

<section class="dark-band abs"></section>
<div class="promo abs" role="img" aria-label="Cappuccino with biscuits and coffee beans"></div>
<div class="promo-text abs">FRESH ROASTED<br>COFFEE<br><span class="promo-btn">SHOP NOW</span></div>

<div class="tabs abs">
  <span class="active">NEW PRODUCTS</span><span class="sep"></span>
  <span>BEST SELLER</span><span class="sep" style="margin-left:26px;margin-right:14px"></span>
  <span>ON SALE PRODUCTS</span>
</div>

<div class="dark-band-products">
  <article class="product abs" style="left:189px;top:1668px">
    <div class="photo ph-dark-silver" role="img" aria-label="Portafilter espresso machine with two glasses"></div>
    <p class="name">Lorem ipsum dolor sit amet,<br>consectetur adipiscing elit,<br>sed do eiusmod tempor</p>
    <div class="tags"><span class="tag new">NEW</span><span class="tag sale">SALE</span></div>
    <div class="rule"></div><div class="rule"></div>
    <p class="price"><s>$120</s><b>$90</b></p>
  </article>
  <article class="product abs" style="left:492px;top:1666px">
    <div class="photo ph-dark-black" role="img" aria-label="Black filter coffee maker with glass jug"></div>
    <p class="name">Lorem ipsum dolor sit amet,<br>consectetur adipiscing elit,<br>sed do eiusmod tempor</p>
    <div class="tags"><span class="tag new">NEW</span><span class="tag sale">SALE</span></div>
    <div class="rule"></div><div class="rule"></div>
    <p class="price"><s>$120</s><b>$90</b></p>
  </article>
  <article class="product abs" style="left:773px;top:1663px">
    <div class="photo ph-dark-steel" role="img" aria-label="Silver automatic espresso machine with latte glass"></div>
    <p class="name">Lorem ipsum dolor sit amet,<br>consectetur adipiscing elit,<br>sed do eiusmod tempor</p>
    <div class="tags"><span class="tag new">NEW</span><span class="tag sale">SALE</span></div>
    <div class="rule"></div><div class="rule"></div>
    <p class="price"><s>$120</s><b>$90</b></p>
  </article>
</div>

<div class="contact-strip abs">Let’s contact:<span class="dot" aria-label="Social link"></span><span class="dot" aria-label="Social link"></span><span class="dot" aria-label="Social link"></span></div>

<footer class="site-footer abs"></footer>
<div class="beans abs" role="img" aria-label="Cluster of roasted coffee beans"></div>
<div class="footer-brand abs">Kornhaus</div>

<div class="f-col abs" style="left:388px">
  <h4>Coffee Store</h4>
  <p>Lorem ipsum dolor</p><p>Lorem ipsum dolor</p><p>Lorem ipsum dolor</p><p>Lorem ipsum dolor</p>
</div>
<div class="f-rule abs" style="left:518px"></div>
<div class="f-col abs" style="left:535px">
  <h4 style="padding-left:28px">Newsletter</h4>
  <p style="line-height:14px">Subscribe to our Newsletter<br><span style="font-size:9px">for Insider Tips &amp; Exclusive Deals!</span></p>
  <div class="news-input">E-mail address</div>
  <span class="news-btn">SUBSCRIBE</span>
</div>
<div class="f-rule abs" style="left:700px"></div>
<div class="f-col abs" style="left:725px">
  <h4>Store Locator</h4>
  <p>Lorem ipsum dolor</p><p>Lorem ipsum dolor</p><p>Lorem ipsum dolor</p><p>Lorem ipsum dolor</p>
</div>
<div class="f-rule abs" style="left:856px"></div>
<div class="f-col abs" style="left:885px;width:190px">
  <h4>Contact Us</h4>
  <p style="line-height:14px">Lorem ipsum dolor sit amet, consectetur adipiscing elit, sed do eiusmod tempor incididunt ut labore et dolore magna aliqua.</p>
  <p style="line-height:15px;margin-top:20px;font-weight:700">hello@kornhaus-roastery.com<br>00/0000000</p>
</div>

</body>
</html>
```